The Perfect Business Card for PineHarbor

I am looking for a business card which beautifully incorporates my logo, reflects my business and looks special, elegant and clean.

```html
<!DOCTYPE html>
<html lang="en">
<head>
<meta charset="utf-8">
<title>PineHarbor Business Card</title>
<link href="https://fonts.googleapis.com/css2?family=Montserrat:wght@400;500;700&display=swap" rel="stylesheet">
<style>
  :root {
    --backdrop: #d6d6d6;
    --card-black: #030303;
    --card-charcoal: #1f1f1f;
    --leaf-green: #6e9a33;
    --edge-green: #4f6b24;
    --text-light: #eeeeee;
    --text-muted: #cfcfcf;
  }
  * { margin: 0; padding: 0; box-sizing: border-box; }
  html, body { width: 1200px; height: 913px; overflow: hidden; background: var(--backdrop); }
  body { position: relative; font-family: "Montserrat", sans-serif; }

  .card {
    position: absolute;
    width: 540px;
    height: 309px;
    border: 2px solid var(--edge-green);
  }
  .card--front { left: 330px; top: 112px; background: var(--card-black); }
  .card--back { left: 330px; top: 492px; background: var(--card-charcoal); overflow: hidden; }

  .brand {
    position: absolute;
    left: 30px;
    top: 160px;
    width: 232px;
    display: flex;
    align-items: center;
    gap: 10px;
    white-space: nowrap;
  }
  .brand__dot {
    width: 26px; height: 26px;
    flex: none;
    border: 2px solid var(--leaf-green);
    border-radius: 50%;
  }
  .brand__name {
    color: var(--leaf-green);
    font-weight: 500;
    font-size: 22px;
    letter-spacing: 0.5px;
    text-transform: uppercase;
  }

  .divider {
    position: absolute;
    left: 280px;
    top: 50px;
    width: 1.5px;
    height: 209px;
    background: var(--edge-green);
  }

  .details { position: absolute; left: 306px; top: 58px; }
  .details__name {
    color: var(--leaf-green);
    font-weight: 700;
    font-size: 24px;
    text-transform: uppercase;
    line-height: 1.1;
  }
  .details__role {
    color: var(--text-muted);
    font-size: 14px;
    margin: 4px 0 18px;
  }
  .contact-list { list-style: none; }
  .contact-list li {
    display: flex;
    align-items: center;
    gap: 9px;
    color: var(--text-light);
    font-size: 13.5px;
    line-height: 24px;
  }
  .contact-list svg { width: 13px; height: 13px; flex: none; }
  .contact-list .address { padding-left: 22px; line-height: 20px; }
  .contact-list .address:first-of-type { margin-top: 4px; }

  .pattern-fill {
    position: absolute;
    inset: 0;
    background: radial-gradient(ellipse at 50% 50%, #2a2a2a 0%, #1c1c1c 70%, #161616 100%);
  }
</style>
</head>
<body>
  <section class="card card--front">
    <div class="brand">
      <span class="brand__dot"></span>
      <span class="brand__name">PineHarbor</span>
    </div>
    <div class="divider"></div>
    <div class="details">
      <h1 class="details__name">Daniel Mercer</h1>
      <p class="details__role">Managing Director</p>
      <ul class="contact-list">
        <li>
          <svg viewBox="0 0 16 16"><path fill="#6e9a33" d="M3.5 1.5l2.5 0 1 3.5-1.6 1.2a8 8 0 0 0 4.4 4.4l1.2-1.6 3.5 1 0 2.5c0 .8-.7 1.5-1.5 1.5C6.8 14 2 9.2 2 3c0-.8.7-1.5 1.5-1.5z"/></svg>
          044-987 650 312
        </li>
        <li>
          <svg viewBox="0 0 16 16"><rect x="1" y="3" width="14" height="10" fill="#6e9a33"/><path d="M1 3l7 5.5L15 3" fill="none" stroke="#030303" stroke-width="1.3"/></svg>
          hello@pineharbor.com
        </li>
        <li>
          <svg viewBox="0 0 16 16"><circle cx="8" cy="8" r="7" fill="#6e9a33"/><path d="M1 8h14M8 1c-2.5 3-2.5 11 0 14M8 1c2.5 3 2.5 11 0 14" fill="none" stroke="#030303" stroke-width="1"/></svg>
          www.pineharbor.com
        </li>
        <li class="address">17 Harbor Walk Lane</li>
        <li class="address">Westbay, 20718</li>
      </ul>
    </div>
  </section>

  <section class="card card--back">
    <div class="pattern-fill" role="img" aria-label="Repeating embossed pattern of the PineHarbor brand mark over charcoal card stock, with one green mark highlighted at the centre"></div>
  </section>
</body>
</html>
```